Tova Brisk Fitness Coaching Project

I am a personal trainer based in London. My services include one-on-one PT sessions, bootcamps.
I would like the design to be minimalistic. With light colours: white, pink, purple.
I specialise in weight loss, flexibility, mobility.

Tova Penrick
Personal Trainer
Email: tova.penrick@mailgrove.net
tel: 07500 918 243
Instagram: Tova Brisk

Target Market(s)

adults, mostly females (age 18-50).

Industry/Entity Type

Fitness

Contact Information for Business Card

Tova Penrick
Personal Trainer
tel: 07500 918 243
Instagram: Tova Brisk

Font styles to use
Serif

Colors
eea4c8
fbd4d5
fdf9cf
cfeae6
cee9f5

Requirements
Nice to have
• minimalistic style
• easy to read and remember

```html
<!DOCTYPE html>
<html lang="en">
<head>
<meta charset="utf-8">
<title>Tova Brisk Fitness Coaching – Business Cards</title>
<link href="https://fonts.googleapis.com/css2?family=Cabin:wght@600;700&family=PT+Serif:ital,wght@1,700&display=swap" rel="stylesheet">
<style>
  :root {
    --backdrop: #3b3b3d;
    --card: #ffffff;
    --pink: #ec0b8d;
    --teal: #1ccfd8;
    --slate: #2c3b42;
    --white: #ffffff;
    --photo-pink: #e51a7d;
    --photo-teal: #24c2c9;
    --photo-dark: #2a3a40;
  }
  * { box-sizing: border-box; margin: 0; padding: 0; }
  html, body { width: 1200px; height: 900px; overflow: hidden; }
  body { background: var(--backdrop); position: relative; font-family: "Cabin", sans-serif; }

  .card {
    position: absolute;
    width: 513px;
    height: 297px;
    border-radius: 24px;
    overflow: hidden;
    background: var(--card);
    box-shadow: 0 6px 14px rgba(0,0,0,.35);
  }
  .card--front-photo { left: 73px; top: 138px; }
  .card--back-white  { left: 615px; top: 138px; }
  .card--front-white { left: 73px; top: 465px; }
  .card--back-photo  { left: 615px; top: 465px; }

  .photo {
    position: absolute; inset: 0;
    background: linear-gradient(180deg,
      var(--photo-pink) 0%, var(--photo-pink) 30%,
      var(--photo-teal) 42%, var(--photo-teal) 72%,
      var(--photo-dark) 90%, var(--photo-dark) 100%);
  }

  .brand-name { font-family: "Cabin", sans-serif; font-weight: 700; line-height: 1; letter-spacing: .5px; }
  .brand-tag  { font-family: "Cabin", sans-serif; font-weight: 700; line-height: 1; letter-spacing: 1px; }
  .serif { font-family: "PT Serif", serif; font-style: italic; font-weight: 700; }

  /* photo front */
  .card--front-photo .brand-block { position: absolute; right: 24px; top: 208px; text-align: right; color: var(--white); }
  .card--front-photo .brand-name { font-size: 38px; }
  .card--front-photo .brand-tag { font-size: 16px; margin-top: 6px; }

  /* white back */
  .card--back-white { text-align: center; }
  .card--back-white .person { position: absolute; left: 0; right: 0; top: 40px; font-size: 15px; line-height: 22px; }
  .person-name { color: var(--pink); text-transform: uppercase; }
  .person-role { color: var(--teal); }
  .card--back-white .brand-name { position: absolute; left: 0; right: 0; top: 98px; font-size: 68px; color: var(--pink); }
  .card--back-white .brand-tag { position: absolute; left: 0; right: 0; top: 181px; font-size: 29px; color: var(--teal); }
  .card--back-white .contacts { position: absolute; left: 0; right: 0; top: 224px; color: var(--slate); font-size: 15.5px; line-height: 21.5px; }

  .contact-line { display: flex; align-items: center; justify-content: center; gap: 6px; }
  .icon { width: 11px; height: 11px; flex: none; }
  .icon--teal { fill: var(--teal); }
  .icon--white { fill: var(--white); }

  /* white front */
  .card--front-white .brand-name { position: absolute; left: 0; right: 0; top: 100px; text-align: center; font-size: 67px; color: var(--pink); }
  .card--front-white .brand-tag { position: absolute; left: 0; right: 0; top: 174px; text-align: center; font-size: 29px; color: var(--teal); }

  /* photo back */
  .card--back-photo .contacts { position: absolute; left: 32px; top: 36px; color: var(--white); font-size: 15.5px; line-height: 22px; }
  .card--back-photo .contact-line { justify-content: flex-start; }
  .card--back-photo .person { position: absolute; right: 26px; top: 151px; text-align: right; color: var(--slate); font-size: 17px; line-height: 25px; }
  .card--back-photo .person-name { color: var(--slate); }
</style>
</head>
<body>

<svg width="0" height="0" style="position:absolute">
  <symbol id="icon-phone" viewBox="0 0 24 24"><path d="M6.6 10.8a15.1 15.1 0 0 0 6.6 6.6l2.2-2.2c.3-.3.7-.4 1-.2 1.1.4 2.3.6 3.6.6.6 0 1 .4 1 1V20c0 .6-.4 1-1 1A17 17 0 0 1 3 4c0-.6.4-1 1-1h3.5c.6 0 1 .4 1 1 0 1.3.2 2.5.6 3.6.1.3 0 .7-.2 1z"/></symbol>
  <symbol id="icon-mail" viewBox="0 0 24 24"><path d="M2 5h20v2l-10 6L2 7z M2 9l10 6 10-6v10H2z"/></symbol>
  <symbol id="icon-square" viewBox="0 0 24 24"><rect x="3" y="3" width="18" height="18" rx="2"/></symbol>
</svg>

<!-- Front with photo -->
<section class="card card--front-photo">
  <div class="photo" role="img" aria-label="Photo of the trainer leaping in front of a pink and turquoise painted wall"></div>
  <div class="brand-block">
    <div class="brand-name">Tova Brisk</div>
    <div class="brand-tag">FITNESS COACHING</div>
  </div>
</section>

<!-- White back with details -->
<section class="card card--back-white">
  <div class="person serif">
    <div class="person-name">Tova Penrick</div>
    <div class="person-role">Personal Trainer</div>
  </div>
  <div class="brand-name">Tova Brisk</div>
  <div class="brand-tag">FITNESS COACHING</div>
  <div class="contacts serif">
    <div class="contact-line"><svg class="icon icon--teal"><use href="#icon-phone"/></svg>07500 918 243</div>
    <div class="contact-line"><svg class="icon icon--teal"><use href="#icon-mail"/></svg>tova.penrick@mailgrove.net</div>
    <div class="contact-line"><svg class="icon icon--teal"><use href="#icon-square"/></svg>Tova Brisk</div>
  </div>
</section>

<!-- White front -->
<section class="card card--front-white">
  <div class="brand-name">Tova Brisk</div>
  <div class="brand-tag">FITNESS COACHING</div>
</section>

<!-- Back with photo -->
<section class="card card--back-photo">
  <div class="photo" role="img" aria-label="Photo of the trainer leaping in front of a pink and turquoise painted wall"></div>
  <div class="contacts serif">
    <div class="contact-line"><svg class="icon icon--white"><use href="#icon-phone"/></svg>07500 918 243</div>
    <div class="contact-line"><svg class="icon icon--white"><use href="#icon-mail"/></svg>tova.penrick@mailgrove.net</div>
    <div class="contact-line"><svg class="icon icon--white"><use href="#icon-square"/></svg>Tova Brisk</div>
  </div>
  <div class="person serif">
    <div class="person-name">Tova Penrick</div>
    <div>Personal Trainer</div>
  </div>
</section>

</body>
</html>
```